Business Card Design for sports performance / psychology company

You can see my website that this is based upon here:
http://www.qtrvantage.co.uk

More than happy to answer any additional questions that you might have

** Happy for any images from Picklevault to be used. If I go with your design I will purchase the image for you to use

Target Market(s)

Football players

Industry/Entity Type

Business

Contact Information for Business Card

Name: Dale Fenwick
Title: Clinical Hypnotherapist & Strategist
Email address: dale@qtrvantage.co.uk
Tel: 07481629054

Font styles to use
Other font styles liked:
• Same font as on website. I'm not actually sure what it is

Requirements
Must have
• Tagline:
• Ability x Form = Performance
• Don't put form down to chance
Nice to have
• Happy for designers to be creative
Should not have

```html
<!DOCTYPE html>
<html lang="en">
<head>
<meta charset="utf-8">
<title>QTR Vantage — Business Card</title>
<link rel="stylesheet" href="https://fonts.googleapis.com/css2?family=Jost:wght@400;500&family=Lato:wght@400;700&display=swap">
<style>
  :root{
    --backdrop:#232323;
    --navy:#241f4b;
    --navy-deep:#1c1840;
    --violet-haze:#4b4770;
    --pitch:#2f4048;
    --white:#ffffff;
    --ink:#2a2650;
  }
  *{box-sizing:border-box;margin:0;padding:0}
  html,body{width:1189px;height:1200px;overflow:hidden;background:var(--backdrop)}
  .sheet{position:relative;width:1189px;height:1200px}
  .card{position:absolute;left:171px;width:855px;height:488px;overflow:hidden}
  .card--front{top:67px}
  .card--back{top:626px;background:var(--white)}

  /* front */
  .stadium-photo{position:absolute;inset:0;
    background:linear-gradient(180deg,#4a4670 0%,#3a3762 38%,#353461 62%,#2d3d4a 66%,#2b3944 100%)}
  .brand-mark{position:absolute;left:388px;top:78px;width:80px;height:80px;border-radius:50%;background:var(--navy);border:3px solid var(--white)}
  .front-name{position:absolute;left:0;right:0;top:177px;text-align:center;
    font-family:"Jost",sans-serif;font-weight:400;font-size:64px;letter-spacing:1px;color:var(--white)}
  .front-tagline{position:absolute;left:0;right:0;top:276px;text-align:center;
    font-family:"Lato",sans-serif;font-size:25px;color:var(--white)}
  .front-url{position:absolute;left:0;right:0;top:406px;text-align:center;
    font-family:"Lato",sans-serif;font-size:21px;color:var(--white)}

  /* back */
  .side-band{position:absolute;left:0;top:0;bottom:0;width:104px;background:var(--navy)}
  .side-rule{position:absolute;left:107px;top:0;bottom:0;width:8px;background:var(--navy)}
  .back-mark{position:absolute;left:42px;top:68px;width:112px;height:112px;border-radius:50%;
    background:var(--navy);box-shadow:0 0 0 10px var(--white)}
  .back-name{position:absolute;left:188px;top:84px;
    font-family:"Jost",sans-serif;font-weight:400;font-size:56px;letter-spacing:1px;color:var(--navy)}
  .person{position:absolute;left:200px;top:276px;font-family:"Lato",sans-serif;color:var(--ink)}
  .person__name{font-size:33px;font-weight:700;line-height:1.1}
  .person__name span{font-weight:400}
  .person__title{font-size:21px;margin-top:2px}
  .contacts{position:absolute;left:200px;top:372px;list-style:none;font-family:"Lato",sans-serif;font-size:23px;color:var(--ink)}
  .contacts li{display:flex;align-items:center;height:28px}
  .contacts svg{width:23px;height:23px;margin-right:10px;flex:none}
</style>
</head>
<body>
<main class="sheet">
  <section class="card card--front">
    <div class="stadium-photo" role="img" aria-label="Blurred floodlit football stadium with the centre circle of the pitch"></div>
    <div class="brand-mark"></div>
    <h1 class="front-name">QTR VANTAGE</h1>
    <p class="front-tagline">Don't Put Form Down To Chance</p>
    <p class="front-url">www.qtrvantage.co.uk</p>
  </section>

  <section class="card card--back">
    <div class="side-band"></div>
    <div class="side-rule"></div>
    <div class="back-mark"></div>
    <h2 class="back-name">QTR VANTAGE</h2>
    <div class="person">
      <p class="person__name">Dale <span>Fenwick</span></p>
      <p class="person__title">Clinical Hypnotherapist &amp; Strategist</p>
    </div>
    <ul class="contacts">
      <li><svg viewBox="0 0 24 24"><rect width="24" height="24" fill="#241f4b"/><path d="M5 10c0-3 14-3 14 0v2h-3v-2H8v2H5z M7 13h10l1 6H6z" fill="#fff"/></svg>07481629054</li>
      <li><svg viewBox="0 0 24 24"><rect width="24" height="24" fill="#241f4b"/><rect x="5" y="7" width="14" height="10" fill="none" stroke="#fff" stroke-width="1.5"/><path d="M5 7l7 6 7-6M5 17l5-5M19 17l-5-5" fill="none" stroke="#fff" stroke-width="1.5"/></svg>dale@qtrvantage.co.uk</li>
      <li><svg viewBox="0 0 24 24"><rect width="24" height="24" fill="#241f4b"/><circle cx="12" cy="12" r="7" fill="none" stroke="#fff" stroke-width="1.4"/><ellipse cx="12" cy="12" rx="3" ry="7" fill="none" stroke="#fff" stroke-width="1.2"/><path d="M5 12h14M6 8.5h12M6 15.5h12" stroke="#fff" stroke-width="1.1"/></svg>www.qtrvantage.co.uk</li>
    </ul>
  </section>
</main>
</body>
</html>
```